I already have a logo created by Quillory Makers that I'm very happy with. I need to spruce up my business card now. Its a double sided card with not much info on it, I like to keep it simple.
Front of card: name, phone # email address, web address. Tag Line "Outsourced Technology Solutions", under that it says Business Voice Services & Electronic Protection.
Rear of Card: Content written inside a "cloud" saying "Cloud Solutions" "Cloud Integrity"

Target Market(s)

Business to Business

Industry/Entity Type

Business

Contact Information for Business Card

We are in the technology field. Providing Telephone systems (hardware), SIP Trunks (dial tone/local/long distance/telephone #'s), LAN (Local Area Network)infrastructure cabling, Data Center solutions and Security Applications (Camera systems, Access Control systems,

Requirements
Must have
• Must have brevity
Should not have
• Clutter and/or too much information

```html
<!DOCTYPE html>
<html lang="en">
<head>
<meta charset="utf-8">
<title>Northwind Relay Networks – Business Card</title>
<link rel="stylesheet" href="https://fonts.googleapis.com/css2?family=Raleway:wght@500;600;700&family=Lato:wght@400;700&display=swap">
<style>
  :root {
    --navy: #1d3f7a;
    --white: #ffffff;
    --grey-text: #7a7f88;
    --page-bg: #e6e6e6;
    --card-shadow: rgba(0, 0, 0, 0.25);
  }
  * { margin: 0; padding: 0; box-sizing: border-box; }
  html, body {
    width: 1200px; height: 1000px; overflow: hidden;
    background: var(--page-bg);
  }
  .canvas { position: relative; width: 1200px; height: 1000px; }
  .card {
    position: absolute; left: 287px; width: 627px; height: 358px;
    box-shadow: 0 6px 14px var(--card-shadow);
  }
  .card-cloud { top: 140px; background: var(--navy); }
  .cloud-shape { position: absolute; left: 0; top: 0; }
  .cloud-tagline {
    position: absolute; left: 0; right: 0; top: 214px;
    text-align: center;
    font-family: 'Raleway', sans-serif; font-weight: 600;
    font-size: 18px; color: var(--navy); letter-spacing: 0.3px;
  }
  .cloud-tagline .sep { margin: 0 10px; font-weight: 500; }

  .card-contact { top: 531px; background: var(--white); }
  .brand { position: absolute; left: 44px; top: 136px; width: 230px; }
  .brand-name {
    display: flex; align-items: center; gap: 8px;
    font-family: 'Raleway', sans-serif; font-weight: 600;
    font-size: 17px; line-height: 1.15; color: var(--navy);
  }
  .brand-mark { width: 12px; height: 12px; background: var(--navy); flex: none; }
  .brand-tagline {
    margin-top: 8px; padding-top: 4px;
    border-top: 1px solid var(--navy);
    font-family: 'Raleway', sans-serif; font-weight: 500;
    font-size: 12.5px; color: var(--grey-text);
  }
  .divider {
    position: absolute; left: 313px; top: 134px;
    width: 1.5px; height: 92px; background: var(--navy); opacity: 0.8;
  }
  .person { position: absolute; left: 337px; top: 128px; }
  .person-name {
    font-family: 'Lato', sans-serif; font-weight: 700;
    font-size: 20px; color: var(--navy);
  }
  .person-title {
    font-family: 'Lato', sans-serif; font-size: 14px;
    color: var(--grey-text); margin-top: 0;
  }
  .contact-list { list-style: none; margin-top: 9px; }
  .contact-list li {
    display: flex; align-items: center; gap: 5px;
    font-family: 'Lato', sans-serif; font-size: 14.5px;
    color: var(--grey-text); line-height: 18px;
  }
  .contact-list svg { width: 11px; height: 11px; fill: var(--navy); flex: none; }
  .service-band {
    position: absolute; left: 0; bottom: 0; width: 100%; height: 36px;
    background: var(--navy); color: var(--white);
    display: flex; align-items: center; justify-content: center;
    font-family: 'Raleway', sans-serif; font-weight: 500; font-size: 14.5px;
  }
</style>
</head>
<body>
<main class="canvas">
  <section class="card card-cloud">
    <svg class="cloud-shape" width="627" height="358" viewBox="0 0 627 358" aria-hidden="true">
      <g fill="#ffffff">
        <circle cx="338" cy="163" r="105"/>
        <circle cx="222" cy="150" r="52"/>
        <rect x="175" y="150" width="100" height="80"/>
        <rect x="133" y="150" width="362" height="150" rx="75" ry="75"/>
      </g>
    </svg>
    <p class="cloud-tagline">Cloud Solutions<span class="sep">|</span>Cloud Integrity</p>
  </section>

  <section class="card card-contact">
    <div class="brand">
      <div class="brand-name"><span class="brand-mark"></span><span>Northwind Relay Networks, LLC</span></div>
      <div class="brand-tagline">Outsourced Technology Solutions</div>
    </div>
    <div class="divider"></div>
    <div class="person">
      <div class="person-name">Alex Moreland</div>
      <div class="person-title">President</div>
      <ul class="contact-list">
        <li><svg viewBox="0 0 24 24"><path d="M6.6 10.8a15 15 0 0 0 6.6 6.6l2.2-2.2a1 1 0 0 1 1-.25 11.4 11.4 0 0 0 3.6.57 1 1 0 0 1 1 1V20a1 1 0 0 1-1 1A17 17 0 0 1 3 4a1 1 0 0 1 1-1h3.5a1 1 0 0 1 1 1c0 1.25.2 2.45.57 3.57a1 1 0 0 1-.25 1z"/></svg>555-014-2277</li>
        <li><svg viewBox="0 0 24 24"><path d="M2 5h20v14H2z"/><path d="M3 6l9 7 9-7" stroke="#fff" stroke-width="2" fill="none"/></svg>hello@northwindrelay.com</li>
        <li><svg viewBox="0 0 24 24"><circle cx="12" cy="12" r="10"/><path d="M2 12h20M12 2c3 3 3 17 0 20M12 2c-3 3-3 17 0 20" stroke="#fff" stroke-width="1.6" fill="none"/></svg>www.northwindrelay.com</li>
      </ul>
    </div>
    <div class="service-band">Business Voice Services &amp; Electronic Protection</div>
  </section>
</main>
</body>
</html>
```